Business card design needed

We are a gardening company who handle:
All Forms of gardens work including
Mowing
Pruning
edging
weeding
Poisoning
Landscaping
Minor Stump Removal
Rubbish Removal
and more

I want a card that look professional not cartoon style

Harlow Yards and Lawncare Service

Dean Marsholt
0486259041

```html
<!DOCTYPE html>
<html lang="en">
<head>
<meta charset="UTF-8">
<title>Harlow Yards and Lawncare Service – Business Card</title>
<link href="https://fonts.googleapis.com/css2?family=Quicksand:wght@300;400;500;700&display=swap" rel="stylesheet">
<style>
  :root {
    --panel: #312c2a;
    --ink: #ffffff;
    --leaf-dark: #0f5a1c;
    --leaf-mid: #23a33a;
    --leaf-light: #5fd36a;
  }
  html, body {
    margin: 0;
    padding: 0;
    width: 1200px;
    height: 693px;
    overflow: hidden;
    background: var(--panel);
  }
  .card {
    position: relative;
    width: 1200px;
    height: 693px;
    background: var(--panel);
    font-family: "Quicksand", sans-serif;
    color: var(--ink);
    overflow: hidden;
  }
  .card__photo {
    position: absolute;
    left: 873px;
    top: 0;
    width: 327px;
    height: 693px;
    background:
      linear-gradient(115deg, var(--leaf-dark) 0%, var(--leaf-mid) 35%, var(--leaf-light) 55%, var(--leaf-mid) 75%, var(--leaf-dark) 100%);
  }
  .card__title {
    position: absolute;
    left: 33px;
    top: 70px;
    margin: 0;
    font-weight: 300;
    font-size: 68px;
    line-height: 85px;
    letter-spacing: 0.06em;
  }
  .card__contact {
    position: absolute;
    left: 34px;
    top: 261px;
    margin: 0;
    font-weight: 300;
    font-size: 42px;
    letter-spacing: 0.06em;
  }
  .card__phone {
    font-weight: 700;
    margin-left: 6px;
  }
  .services {
    position: absolute;
    left: 35px;
    top: 492px;
    margin: 0;
  }
  .services__heading {
    margin: 0 0 2px;
    font-weight: 700;
    font-size: 29px;
    line-height: 36px;
    letter-spacing: 0.07em;
  }
  .services__list {
    margin: 0;
    font-weight: 400;
    font-size: 26px;
    line-height: 34px;
    letter-spacing: 0.08em;
  }
  .services__more {
    font-style: italic;
  }
</style>
</head>
<body>
  <div class="card">
    <h1 class="card__title">Harlow Yards<br>and Lawncare Service</h1>
    <p class="card__contact">Dean Marsholt<span class="card__phone">0486259041</span></p>

    <div class="services">
      <p class="services__heading">All forms of garden work</p>
      <p class="services__list">
        including mowing, pruning, edging<br>
        weeding, poisoning, landscaping<br>
        minor stump removal, rubbish removal<br>
        <span class="services__more">and more</span>
      </p>
    </div>

    <div class="card__photo" role="img" aria-label="Close-up photo of green grass blades covered in water droplets"></div>
  </div>
</body>
</html>
```